Business Card Design

We need a new business card design for a CPA office that has been in business for over 10 years. We are a Accounting Concierge firm that offers the following services: Certified Public Accountant, Personal & Business Tax Preparation, Accounting, Bookkeeping, Payroll Services, Tax Litigation Services.
Certified LedgerNest CertPartner.  We would like to see designs that use the color navy blue in the company logo with classic accent colors.  We would like the card to be on a textured high pound card stock and that is more classic and less modern in design.  The final design should communicate class and professionalism.

Reason: I gave feedback to many of the designers with some changes.  Please re-read the brief as we would like to remove the photo of the man on the card.  We also want only light grey or white background, not navy or blue - the navy or blue tones should be the font or accent colors.  Please also, consider creating a logo with the initials P&W or PW or P&W CPA.

Industry/Entity Type
Business
Contact Information for Business Card
Pellford & Company CPA, Dominic Pellford III, 4317 Larkmoor Road, Suite D, Bradenton, FL  34519, Phone: (941) 555-0137, Fax: (941) 555-0182, Email: Dominic@DPellfordCPA.example, Website: www.DPellfordCPA.example
Requirements
Must have
- LedgerNest Logo

Should not have
- we no longer want the photo on the card.

```html
<!DOCTYPE html>
<html lang="en">
<head>
<meta charset="utf-8">
<title>Pellford &amp; Company CPA — Business Card</title>
<link rel="stylesheet" href="https://fonts.googleapis.com/css2?family=Marcellus&family=Raleway:wght@500&family=Oswald:wght@600&family=Tinos&display=swap">
<style>
  :root {
    --navy: #1b1f4a;
    --navy-deep: #141838;
    --ink: #1c1c1f;
    --rule: #8e8e92;
    --paper: #eeeeec;
    --paper-shade: #e2e2df;
    --backdrop: #ffffff;
    --badge: #b9b9bc;
  }
  * { margin: 0; padding: 0; box-sizing: border-box; }
  html, body { width: 1200px; height: 900px; overflow: hidden; background: var(--backdrop); }
  .card {
    position: absolute; left: 75px; top: 150px; width: 1050px; height: 600px;
    border-radius: 34px;
    background:
      radial-gradient(circle at 30% 40%, rgba(255,255,255,.55), transparent 60%),
      linear-gradient(135deg, var(--paper), var(--paper-shade));
    box-shadow: 0 10px 30px rgba(0,0,0,.18);
    overflow: hidden;
  }
  .brand-mark {
    position: absolute; left: 52px; top: 44px; width: 186px; height: 186px;
    border-radius: 22px; background: var(--navy);
    box-shadow: 0 3px 8px rgba(0,0,0,.35);
  }
  .firm-name {
    position: absolute; left: 262px; top: 64px;
    font-family: "Marcellus", serif; font-size: 50px; color: var(--navy); white-space: nowrap;
  }
  .firm-rule {
    position: absolute; left: 264px; top: 148px; width: 494px; height: 3px; background: var(--rule);
  }
  .firm-tagline {
    position: absolute; left: 264px; top: 160px;
    font-family: "Raleway", sans-serif; font-weight: 500; font-size: 23px;
    letter-spacing: 5.4px; color: var(--ink); white-space: nowrap;
  }
  .services-band {
    position: absolute; left: 0; top: 244px; width: 100%; height: 28px;
    background: var(--navy-deep); color: #fff;
    font-family: "Oswald", sans-serif; font-weight: 600; font-size: 15.5px;
    line-height: 28px; padding-left: 58px; white-space: nowrap; letter-spacing: .2px;
  }
  .person-name {
    position: absolute; left: 58px; top: 290px;
    font-family: "Tinos", serif; font-size: 40px; color: var(--navy);
  }
  .person-title {
    position: absolute; left: 58px; top: 346px;
    font-family: "Tinos", serif; font-size: 22px; color: var(--ink);
  }
  .contact-list {
    position: absolute; left: 58px; top: 392px; list-style: none;
    font-family: "Tinos", serif; font-size: 27px; color: var(--ink);
  }
  .contact-list li { display: flex; align-items: center; height: 38px; }
  .contact-list svg { width: 26px; height: 26px; margin-right: 8px; fill: var(--navy); flex: none; }
  .partner-badge {
    position: absolute; right: 66px; top: 422px; width: 32px; height: 58px;
    background: var(--badge); border-radius: 2px;
  }
</style>
</head>
<body>
  <div class="card">
    <div class="brand-mark" aria-hidden="true"></div>
    <h1 class="firm-name">Pellford &amp; Company CPA</h1>
    <div class="firm-rule"></div>
    <p class="firm-tagline">Certified Public Accountant</p>

    <div class="services-band">CERTIFIED PUBLIC ACCOUNTANT, PERSONAL &amp; BUSINESS TAX PREPARATION, ACCOUNTING, BOOKKEEPING, PAYROLL SERVICES, TAX LITIGATION SERVICES.</div>

    <h2 class="person-name">Dominic Pellford III</h2>
    <p class="person-title">Director</p>

    <ul class="contact-list">
      <li><svg viewBox="0 0 24 24"><path d="M6.6 10.8a15.1 15.1 0 0 0 6.6 6.6l2.2-2.2a1 1 0 0 1 1-.25 11.4 11.4 0 0 0 3.6.57 1 1 0 0 1 1 1V20a1 1 0 0 1-1 1A17 17 0 0 1 3 4a1 1 0 0 1 1-1h3.5a1 1 0 0 1 1 1c0 1.25.2 2.45.57 3.57a1 1 0 0 1-.25 1z"/></svg>(941) 555-0137</li>
      <li><svg viewBox="0 0 24 24"><path d="M7 3h8l3 3v4H7z M4 10h16a2 2 0 0 1 2 2v6h-4v3H6v-3H2v-6a2 2 0 0 1 2-2z M8 15v4h8v-4z"/></svg>(941) 555-0182</li>
      <li><svg viewBox="0 0 24 24"><path d="M2 6h20v12H2z M3 7l9 7 9-7" stroke="#eeeeec" stroke-width="1.5"/></svg>Dominic@DPellfordCPA.example</li>
      <li><svg viewBox="0 0 24 24"><path d="M12 2a10 10 0 1 0 0 20 10 10 0 0 0 0-20zm0 2c1.2 1.5 2 3.6 2.2 6H9.8c.2-2.4 1-4.5 2.2-6zM4.1 10h3.7c.1-2.1.7-4 1.5-5.5A8 8 0 0 0 4.1 10zm0 4a8 8 0 0 0 5.2 5.5c-.8-1.5-1.4-3.4-1.5-5.5zm5.7 0c.2 2.4 1 4.5 2.2 6 1.2-1.5 2-3.6 2.2-6zm6.4 0c-.1 2.1-.7 4-1.5 5.5a8 8 0 0 0 5.2-5.5zm3.7-4a8 8 0 0 0-5.2-5.5c.8 1.5 1.4 3.4 1.5 5.5z"/></svg>www.DPellfordCPA.example</li>
      <li><svg viewBox="0 0 24 24"><path d="M12 3l10 9h-3v9h-5v-6h-4v6H5v-9H2z"/></svg>4317 Larkmoor Road, Suite D, Bradenton, FL 34519</li>
    </ul>

    <div class="partner-badge" role="img" aria-label="LedgerNest CertPartner certification badge"></div>
  </div>
</body>
</html>
```